Business Card, Stationary, Fax Cover, and Email Signature
Telvar Capital
Professional
Derek Hollow
President/Founder
418 Bramble Creek Lane, Suite 327
Marlow Ridge, VA 20999
dhollow@telvarcapital.example
www.TelvarCapital.example
Credit Repair - Credit Restoration - Credit Education ( Centered Top)
Legally And Ethically Remove Derogatory Items From Your Credit Report (Bullet Point)
Help Establish New Positive Trade Lines
(Bullet Point)
Learn How To Maintain And Increase Your Credit Score (Bullet Point)
www.TelvarCapital.example (Centered Bottom)

```html
<!DOCTYPE html>
<html lang="en">
<head>
<meta charset="utf-8">
<title>Telvar Capital – Business Card</title>
<link rel="stylesheet" href="https://fonts.googleapis.com/css2?family=Arimo:wght@400;700&display=swap">
<style>
  :root {
    --backdrop: #e4e6ea;
    --card: #ffffff;
    --brand-navy: #1c3d8c;
    --brand-blue: #2b63c2;
    --arc-grey: #b9bdc6;
    --ink: #4d4f55;
    --divider: #8a8d94;
  }
  * { box-sizing: border-box; margin: 0; padding: 0; }
  html, body {
    width: 1200px; height: 780px; overflow: hidden;
    background: var(--backdrop);
    font-family: "Arimo", Arial, sans-serif;
  }
  .business-card {
    position: absolute; left: 80px; top: 90px;
    width: 1040px; height: 600px;
    background: var(--card);
    border-radius: 32px;
    overflow: hidden;
    box-shadow: 0 6px 18px rgba(0,0,0,0.18);
  }
  .card-swooshes { position: absolute; inset: 0; }
  .brand-lockup {
    position: absolute; left: 240px; top: 120px;
    display: flex; align-items: center; gap: 26px;
  }
  .brand-dot {
    width: 140px; height: 140px; border-radius: 50%;
    background: var(--brand-blue);
  }
  .brand-name {
    font-size: 66px; font-weight: 400; color: var(--brand-navy);
    letter-spacing: 1px;
  }
  .identity {
    position: absolute; right: 560px; top: 368px;
    text-align: right; color: var(--ink);
  }
  .identity .person-name {
    font-size: 30px; font-weight: 700; color: var(--brand-navy);
    margin-bottom: 4px;
  }
  .identity .person-title { font-size: 21px; margin-bottom: 14px; }
  .identity .address-line { font-size: 19px; line-height: 27px; }
  .column-divider {
    position: absolute; left: 500px; top: 370px;
    width: 2px; height: 170px; background: var(--divider);
  }
  .contact-list {
    position: absolute; left: 524px; top: 366px;
    list-style: none; color: var(--ink); font-size: 19px;
  }
  .contact-list li {
    display: flex; align-items: center; gap: 12px;
    height: 35px;
  }
  .contact-icon { width: 20px; height: 20px; flex: none; }
  .contact-icon path, .contact-icon rect, .contact-icon circle { fill: var(--brand-navy); }
</style>
</head>
<body>
  <div class="business-card">
    <svg class="card-swooshes" width="1040" height="600" viewBox="0 0 1040 600" aria-hidden="true">
      <defs>
        <linearGradient id="swoosh-blue" x1="0" y1="0" x2="1" y2="1">
          <stop offset="0" stop-color="#3a76d6"/>
          <stop offset="1" stop-color="#143079"/>
        </linearGradient>
      </defs>
      <path d="M0,80 C95,150 100,290 0,380" fill="none" stroke="var(--arc-grey)" stroke-width="4"/>
      <path d="M0,95 C70,155 78,280 0,355 Z" fill="url(#swoosh-blue)"/>
      <path d="M0,455 C70,515 160,575 290,600" fill="none" stroke="var(--arc-grey)" stroke-width="4"/>
      <path d="M0,478 C60,530 140,578 250,600 L0,600 Z" fill="url(#swoosh-blue)"/>
      <path d="M1040,55 C935,180 935,420 1040,545" fill="none" stroke="var(--arc-grey)" stroke-width="4"/>
      <path d="M1040,80 C962,185 962,415 1040,520 Z" fill="url(#swoosh-blue)"/>
    </svg>

    <div class="brand-lockup">
      <div class="brand-dot"></div>
      <div class="brand-name">Telvar Capital</div>
    </div>

    <div class="identity">
      <div class="person-name">Derek Hollow</div>
      <div class="person-title">President/Founder</div>
      <div class="address-line">418 Bramble Creek Lane</div>
      <div class="address-line">Suite 327</div>
      <div class="address-line">Marlow Ridge, VA 20999</div>
    </div>

    <div class="column-divider"></div>

    <ul class="contact-list">
      <li>
        <svg class="contact-icon" viewBox="0 0 20 20" aria-hidden="true"><path d="M5 1 L8 5 L6 7.5 C7 10 9.5 12.5 12 13.5 L14.5 11.5 L19 14.5 L17 18.5 C9 18.5 1.5 11 1.5 3 Z"/></svg>
        <span>(800) 555-0147</span>
      </li>
      <li>
        <svg class="contact-icon" viewBox="0 0 20 20" aria-hidden="true"><path d="M5 1 L8 5 L6 7.5 C7 10 9.5 12.5 12 13.5 L14.5 11.5 L19 14.5 L17 18.5 C9 18.5 1.5 11 1.5 3 Z"/></svg>
        <span>(703) 555-0162</span>
      </li>
      <li>
        <svg class="contact-icon" viewBox="0 0 20 20" aria-hidden="true"><rect x="5" y="1" width="10" height="6"/><rect x="1" y="8" width="18" height="8" rx="2"/><rect x="5" y="14" width="10" height="5"/></svg>
        <span>(703) 555-0189</span>
      </li>
      <li>
        <svg class="contact-icon" viewBox="0 0 20 20" aria-hidden="true"><path d="M1 4 H19 V16 H1 Z M2.5 5.5 L10 11 L17.5 5.5 V6.5 L10 12.3 L2.5 6.5 Z" fill-rule="evenodd"/></svg>
        <span>dhollow@telvarcapital.example</span>
      </li>
      <li>
        <svg class="contact-icon" viewBox="0 0 20 20" aria-hidden="true"><circle cx="10" cy="10" r="9"/></svg>
        <span>www.TelvarCapital.example</span>
      </li>
    </ul>
  </div>
</body>
</html>
```